New corporate e-mail signature

We need a new e-mail signature for our company that is clean and professional. The requests are attached in a document.

Target Market(s)

CFO, CTO, Controllers, leaders, decision-makers.

Industry/Entity Type

Information Technology

Colors

Designer to choose colors to be used in the design.

Requirements
Must have
• See the PowerPoint document.
• - keep it as simple as possible.
• - same style as our new website design
• - It has to look good in all e-mail readers, and on all surfaces.
Nice to have
• - Please also attach 'best practise' for how to use the signature.
Should not have
• See the PowerPoint document. Use our color palette.
• - Do not include photo!

```html
<!DOCTYPE html>
<html lang="en">
<head>
<meta charset="utf-8">
<title>Northvale E-mail Signature</title>
<link href="https://fonts.googleapis.com/css2?family=Montserrat:wght@500;600;700;800&display=swap" rel="stylesheet">
<style>
  :root {
    --bg: #ffffff;
    --ink: #1d2733;
    --accent: #0e6a8e;
    --accent-deep: #0b4f6e;
    --teal: #2a8c9a;
    --rule: #c9d3da;
    --white: #ffffff;
  }
  * { margin: 0; padding: 0; box-sizing: border-box; }
  html, body {
    width: 1200px; height: 817px; overflow: hidden;
    background: var(--bg);
    font-family: "Montserrat", Arial, sans-serif;
  }
  .signature {
    position: absolute;
    left: 120px; top: 252px;
    width: 960px; height: 313px;
    display: flex;
  }
  .signature__details {
    position: relative;
    width: 570px; height: 313px;
    padding: 70px 0 0 34px;
    background: var(--white);
  }
  .signature__details::after {
    content: "";
    position: absolute; left: 0; right: 80px; bottom: -26px; height: 40px;
    background: radial-gradient(ellipse at 50% 0%, rgba(0,0,0,0.14), rgba(0,0,0,0) 70%);
  }
  .signature__name {
    font-size: 33px; font-weight: 700; color: var(--accent);
    letter-spacing: 0.2px;
  }
  .signature__role {
    margin-top: 6px;
    font-size: 23px; font-weight: 500; color: var(--ink);
  }
  .signature__contacts {
    margin-top: 40px; list-style: none;
  }
  .signature__contact {
    display: flex; align-items: center; gap: 12px;
    font-size: 22px; font-weight: 600; color: var(--accent);
    margin-bottom: 14px;
  }
  .signature__contact svg { width: 22px; height: 22px; flex: none; }
  .signature__divider {
    width: 3px; height: 313px; background: var(--rule);
    margin-right: 5px;
  }
  .signature__brand {
    position: relative;
    width: 382px; height: 313px;
    overflow: hidden;
  }
  .signature__brand-photo {
    position: absolute; inset: 0;
    background: linear-gradient(160deg, var(--accent-deep) 0%, var(--teal) 55%, #5aa7b5 100%);
  }
  .signature__brand-content {
    position: relative;
    padding: 110px 0 0 40px;
    color: var(--white);
  }
  .signature__wordmark {
    font-size: 36px; font-weight: 800; letter-spacing: -0.5px;
  }
  .signature__web {
    margin-top: 14px;
    font-size: 17px; font-weight: 600;
  }
  .signature__social {
    display: flex; gap: 34px; margin-top: 42px;
  }
  .signature__social-dot {
    width: 26px; height: 26px; border-radius: 50%;
    background: var(--white);
  }
</style>
</head>
<body>
  <section class="signature">
    <div class="signature__details">
      <p class="signature__name">Daniel Marlowe</p>
      <p class="signature__role">Business Analyst</p>
      <ul class="signature__contacts">
        <li class="signature__contact">
          <svg viewBox="0 0 24 24" aria-hidden="true"><rect x="3" y="6" width="18" height="12" rx="2" fill="none" stroke="#0e6a8e" stroke-width="2"/><path d="M3.5 7l8.5 6 8.5-6" fill="none" stroke="#0e6a8e" stroke-width="2"/></svg>
          daniel@northvale.com
        </li>
        <li class="signature__contact">
          <svg viewBox="0 0 24 24" aria-hidden="true"><path d="M6.6 3.5l3 3.2-1.8 2.4a13 13 0 006.9 6.9l2.4-1.8 3.2 3-1.6 2.9C12.9 20.6 3.4 11.1 3.7 5.2z" fill="#0e6a8e"/></svg>
          001 555 204 318
        </li>
      </ul>
    </div>
    <div class="signature__divider"></div>
    <div class="signature__brand">
      <div class="signature__brand-photo" role="img" aria-label="Photograph of a modern glass office building facade in blue and teal tones"></div>
      <div class="signature__brand-content">
        <p class="signature__wordmark">northvale</p>
        <p class="signature__web">www.northvale.com</p>
        <div class="signature__social" aria-label="Social media links">
          <span class="signature__social-dot"></span>
          <span class="signature__social-dot"></span>
          <span class="signature__social-dot"></span>
        </div>
      </div>
    </div>
  </section>
</body>
</html>
```